Shipping container company needs 7 print ads developed

We sell and rent shipping containers as affordable storage solutions.Target markets are agricultural, construction, commercial, warehouse, manufacturing, and hobby farms. I need seven persona -specific (see attached 7 personas) clean minimalistic 4.375" x 4" ads in color with graphics, copy, 20' stock container image, and logo. Also, see attached brand guidelines.. Special note -phone number needs to be changed to 555.014.3829

```html
<!DOCTYPE html>
<html lang="en">
<head>
<meta charset="utf-8">
<title>Ridgeline Containers – Print Ads</title>
<link href="https://fonts.googleapis.com/css2?family=Poppins:wght@500;600;700&display=swap" rel="stylesheet">
<style>
  :root {
    --backdrop: #e1e1e1;
    --teal: #0c8e8b;
    --teal-light: #5bbaa8;
    --navy: #10213a;
    --white: #ffffff;
    --bullet: #7fcbb8;
  }
  * { box-sizing: border-box; margin: 0; padding: 0; }
  html, body {
    width: 1200px; height: 474px; overflow: hidden;
    background: var(--backdrop);
    font-family: "Poppins", sans-serif;
  }
  .ad {
    position: absolute; top: 81px;
    width: 318px; height: 290px; overflow: hidden;
    background: radial-gradient(circle at 50% 45%, var(--teal-light) 0%, var(--teal) 55%, var(--teal) 100%);
  }
  .ad--protect { left: 78px; }
  .ad--affordable { left: 448px; }
  .ad--workflow { left: 804px; }
  .ad__shapes { position: absolute; inset: 0; width: 318px; height: 290px; }
  .ad__headline {
    position: absolute;
    display: flex; align-items: center; justify-content: center;
    background: var(--navy); color: var(--white);
    font-weight: 600; white-space: nowrap;
  }
  .ad--protect .ad__headline { left: 17px; top: 18px; width: 283px; height: 26px; font-size: 21px; }
  .ad--affordable .ad__headline { left: 14px; top: 16px; width: 288px; height: 29px; font-size: 17px; }
  .ad--workflow .ad__headline { left: 14px; top: 13px; width: 288px; height: 32px; font-size: 17px; }
  .ad__subline {
    position: absolute; left: 0; width: 318px; text-align: center;
    color: var(--white); font-weight: 600; line-height: 20px;
    white-space: nowrap;
  }
  .ad--protect .ad__subline { top: 47px; font-size: 18px; }
  .ad--affordable .ad__subline { top: 45px; font-size: 15.8px; }
  .ad--workflow .ad__subline { top: 45px; font-size: 18px; }
  .ad__benefits {
    position: absolute; list-style: none;
    color: var(--white); font-weight: 600; font-size: 10px; line-height: 15px;
    text-transform: uppercase; white-space: nowrap;
  }
  .ad--protect .ad__benefits { left: 23px; top: 89px; }
  .ad--affordable .ad__benefits { left: 22px; top: 74px; }
  .ad--workflow .ad__benefits { left: 22px; top: 74px; }
  .ad__benefits li { position: relative; padding-left: 11px; }
  .ad__benefits li.is-wrapped { line-height: 12px; padding-top: 1px; padding-bottom: 2px; }
  .ad__benefits li::before {
    content: ""; position: absolute; left: 0; top: 4px;
    width: 6px; height: 6px; background: var(--bullet);
  }
  .ad__photo { position: absolute; }
  .ad__brand {
    position: absolute; left: 24px; top: 240px;
    display: flex; align-items: center; gap: 7px;
    color: var(--navy); font-weight: 700; font-size: 15px; line-height: 17px;
  }
  .ad__brand-mark { width: 14px; height: 14px; background: var(--navy); flex: none; }
  .ad__cta {
    position: absolute; left: 219px; top: 254px;
    display: flex; align-items: center; gap: 5px;
    color: var(--navy); font-weight: 700; font-size: 12.5px;
  }
</style>
</head>
<body>

<section class="ad ad--protect">
  <svg class="ad__shapes" viewBox="0 0 318 290" aria-hidden="true">
    <polygon points="99,207 318,64 318,207" fill="#10213a"/>
    <polygon points="0,182 30,198 0,214" fill="#10213a"/>
    <polygon points="0,210 54,182 99,207 318,207 318,290 0,290" fill="#ffffff"/>
  </svg>
  <h2 class="ad__headline">Protect Your Investments</h2>
  <p class="ad__subline">with our&nbsp; 20ft steel containers</p>
  <ul class="ad__benefits">
    <li>Durable and weather resistant</li>
    <li>Quick turnaround</li>
    <li>No hidden fees</li>
  </ul>
  <div class="ad__photo" role="img" aria-label="Red shipping container behind the blue one"
       style="left:248px; top:96px; width:70px; height:60px; background:linear-gradient(120deg,#c62a25,#b81f1c);"></div>
  <div class="ad__photo" role="img" aria-label="Blue 20ft steel shipping container"
       style="left:128px; top:120px; width:164px; height:120px; background:linear-gradient(110deg,#1f47b0 0%,#2a56c4 70%,#1d3f99 100%);"></div>
  <div class="ad__brand"><span class="ad__brand-mark"></span>Ridgeline Containers</div>
  <div class="ad__cta">Buy Online
    <svg width="11" height="9" viewBox="0 0 11 9" aria-hidden="true"><path d="M1 5l3 3 6-7" fill="none" stroke="#10213a" stroke-width="2"/></svg>
  </div>
</section>

<section class="ad ad--affordable">
  <svg class="ad__shapes" viewBox="0 0 318 290" aria-hidden="true">
    <polygon points="99,207 318,64 318,207" fill="#10213a"/>
    <polygon points="0,182 30,198 0,214" fill="#10213a"/>
    <polygon points="0,210 54,182 99,207 318,207 318,290 0,290" fill="#ffffff"/>
  </svg>
  <h2 class="ad__headline">Affordable shipping containers</h2>
  <p class="ad__subline">for safer, more efficient job sites</p>
  <ul class="ad__benefits">
    <li>Heavy-duty locks</li>
    <li>Customizable</li>
    <li>Quick turnaround</li>
    <li>Fast communication</li>
    <li>Efficent support</li>
  </ul>
  <div class="ad__photo" role="img" aria-label="Stack of red, yellow and green shipping containers"
       style="left:199px; top:66px; width:111px; height:176px; background:linear-gradient(180deg,#c23a36 0%,#c23a36 33%,#dcc12e 36%,#dcc12e 66%,#3f7a5c 69%,#3a6f55 100%);"></div>
  <div class="ad__brand"><span class="ad__brand-mark"></span>Ridgeline Containers</div>
  <div class="ad__cta">Buy Online
    <svg width="11" height="9" viewBox="0 0 11 9" aria-hidden="true"><path d="M1 5l3 3 6-7" fill="none" stroke="#10213a" stroke-width="2"/></svg>
  </div>
</section>

<section class="ad ad--workflow">
  <svg class="ad__shapes" viewBox="0 0 318 290" aria-hidden="true">
    <polygon points="99,207 318,64 318,207" fill="#10213a"/>
    <polygon points="0,182 30,198 0,214" fill="#10213a"/>
    <polygon points="0,210 54,182 99,207 318,207 318,290 0,290" fill="#ffffff"/>
  </svg>
  <h2 class="ad__headline">Improve Workflow Efficiency</h2>
  <p class="ad__subline">with Ridgeline Containers</p>
  <ul class="ad__benefits">
    <li>Secure and durable</li>
    <li class="is-wrapped">Transparent pricing<br>and rental options</li>
    <li>Quick turnaround</li>
    <li>Efficent support</li>
  </ul>
  <div class="ad__photo" role="img" aria-label="Blue-grey shipping container resting on a red container, seen from below"
       style="left:156px; top:75px; width:148px; height:132px; background:linear-gradient(160deg,#6f7fb4 0%,#8d9dcc 45%,#c74a45 60%,#b83a36 100%);"></div>
  <div class="ad__brand"><span class="ad__brand-mark"></span>Ridgeline Containers</div>
  <div class="ad__cta">Buy Online
    <svg width="11" height="9" viewBox="0 0 11 9" aria-hidden="true"><path d="M1 5l3 3 6-7" fill="none" stroke="#10213a" stroke-width="2"/></svg>
  </div>
</section>

</body>
</html>
```